Lantern Hill Publicity is a new boutique Press Office with a small roster of well-chosen clients across an array of disciplines; from Art and Technology to Restaurants and Fashion. Based in Greenpoint Brooklyn, Lantern Hill Publicity achieves outstanding results through hard work, tenacity, efficiency and a sense of humor. We need a simple, versatile and classic design. We would like each side of the card to be white text on a black background.

Boutique

```html
<!DOCTYPE html>
<html lang="en">
<head>
<meta charset="utf-8">
<title>Lantern Hill Publicity — Business Card</title>
<link href="https://fonts.googleapis.com/css2?family=Cinzel:wght@400&family=Open+Sans:wght@400;700&display=swap" rel="stylesheet">
<style>
  :root {
    --stage-light: #9a9a9a;
    --stage-dark: #4a4a4a;
    --card-black: #121212;
    --card-sheen: #262626;
    --ink-white: #ffffff;
    --ink-soft: #e4e4e4;
    --band-white: #ffffff;
    --ink-black: #111111;
  }
  * { box-sizing: border-box; margin: 0; padding: 0; }
  html, body { width: 1200px; height: 950px; overflow: hidden; }
  body {
    background: radial-gradient(ellipse at 50% 40%, var(--stage-light) 0%, var(--stage-dark) 100%);
    position: relative;
    font-family: "Open Sans", Arial, sans-serif;
  }
  .card {
    position: absolute;
    left: 250px;
    width: 700px;
    height: 400px;
    border-radius: 22px;
    background: linear-gradient(160deg, var(--card-sheen) 0%, var(--card-black) 55%);
    box-shadow: 0 14px 30px rgba(0,0,0,0.45);
    overflow: hidden;
    color: var(--ink-white);
  }
  .card--front { top: 55px; }
  .card--back { top: 495px; }

  .wordmark {
    font-family: "Cinzel", "Times New Roman", serif;
    font-weight: 400;
    text-align: center;
    line-height: 1;
  }
  .wordmark__name { font-size: 38px; letter-spacing: 6px; }
  .wordmark__sub { font-size: 15px; letter-spacing: 9px; margin-top: 8px; }

  .card--front .wordmark {
    position: absolute;
    top: 50%; left: 0; right: 0;
    transform: translateY(-50%);
    color: var(--ink-white);
  }

  .band {
    position: absolute;
    top: 58px; left: 0; right: 0;
    height: 122px;
    background: var(--band-white);
    display: flex;
    align-items: center;
    justify-content: center;
  }
  .band .wordmark { color: var(--ink-black); }

  .contact {
    position: absolute;
    top: 212px; left: 0; right: 0;
    text-align: center;
    color: var(--ink-soft);
    font-size: 15px;
    line-height: 1.55;
  }
  .contact__person { font-size: 19px; color: var(--ink-white); }
  .contact__name { font-weight: 700; letter-spacing: 0.5px; }
  .contact__role { font-weight: 400; font-size: 16px; }
  .contact__row {
    display: flex;
    justify-content: center;
    align-items: center;
    gap: 6px;
  }
  .contact__row .gap { width: 10px; }
  .icon { width: 14px; height: 14px; fill: var(--ink-white); flex: none; }
</style>
</head>
<body>

  <section class="card card--front" aria-label="Card front">
    <div class="wordmark">
      <div class="wordmark__name">LANTERN HILL</div>
      <div class="wordmark__sub">PUBLICITY</div>
    </div>
  </section>

  <section class="card card--back" aria-label="Card back">
    <div class="band">
      <div class="wordmark">
        <div class="wordmark__name">LANTERN HILL</div>
        <div class="wordmark__sub">PUBLICITY</div>
      </div>
    </div>

    <div class="contact">
      <p class="contact__person"><span class="contact__name">MARCUS HALE</span> <span class="contact__role">- CEO/Founder</span></p>
      <p>hello@lanternhillpr.com</p>
      <p>214 Franklin Street, Brooklyn, NY 11222</p>
      <p class="contact__row">
        <svg class="icon" viewBox="0 0 16 16" aria-hidden="true"><path d="M3.6 1.5l2.3 2.6-1.3 1.8c.9 2 2.5 3.6 4.5 4.5l1.8-1.3 2.6 2.3-1.3 2.1C7.3 13.6 2.4 8.7 1.5 3.8z"/></svg>
        <span>718 555 0142</span><span class="gap"></span>
        <svg class="icon" viewBox="0 0 16 16" aria-hidden="true"><path d="M4.5 1h7a1 1 0 0 1 1 1v12a1 1 0 0 1-1 1h-7a1 1 0 0 1-1-1V2a1 1 0 0 1 1-1zm.5 2v9h6V3zm3 10a.8.8 0 1 0 0 1.6.8.8 0 0 0 0-1.6z"/></svg>
        <span>917 555 0187</span><span class="gap"></span>
        <svg class="icon" viewBox="0 0 16 16" aria-hidden="true"><path d="M4 1h6v4H4zM2 6h12a1 1 0 0 1 1 1v6a1 1 0 0 1-1 1H2a1 1 0 0 1-1-1V7a1 1 0 0 1 1-1zm2 5v1h8v-1z"/></svg>
        <span>718 555 0199</span>
      </p>
      <p class="contact__row">
        <svg class="icon" viewBox="0 0 16 16" aria-hidden="true"><path d="M8 1a7 7 0 1 0 0 14A7 7 0 0 0 8 1zm-1 2.2v1.5L5.3 6.4 3 5.6A5.5 5.5 0 0 1 7 3.2zm4.8 8.5l-1.6-1.1V9L8.6 8 6.8 9.2 7.5 12l-.2 1.4a5.5 5.5 0 0 1-4.7-5l1.8.9 1.6-.6L9 5.2l1.8.4 1.8 2.1a5.5 5.5 0 0 1-.8 4z"/></svg>
        <span>www.lanternhillpr.com</span>
      </p>
    </div>
  </section>

</body>
</html>
```